London Street Food business requires a promotional newspaper Ad

We are looking to run an Ad in The Harbour Courier newspaper to promote our business and boost our private events.
The specifications are - format: A hires. jpeg measurements: 20x3 (240mm high x 151 mm) There should be empasis on the social media, food and logo. We are looking to have a simple promotion, maybe with a keyword, that potential customers can quote and receive 10% off. This offer would expire end of March 2017. Also included in the Ad the places we have been featured/mentioned. Our business colors are blue and white. Have a peak at our website: www.thesizzlingpelican.co.uk

Target Market(s)

Any one that wants to have something unique for their event (corporate, weddings, charities, family celebrations)

Industry/Entity Type

Catering

Requirements
Must have
• clear, bold, to the point , eye catching. modern, fresh
Nice to have
• quality of the food comes through,
Should not have
• cheesy greek designs (using greek letters, reference to ancient ruins)

```html
<!DOCTYPE html>
<html lang="en">
<head>
<meta charset="utf-8">
<title>The Sizzling Pelican – Newspaper Ad</title>
<link rel="stylesheet" href="https://fonts.googleapis.com/css2?family=Questrial&family=Arimo:wght@400&display=swap">
<style>
  :root {
    --brand-blue: #3461ad;
    --offer-red: #c8442b;
    --paper: #ffffff;
    --backdrop: #eeeeee;
    --body-ink: #4a4a4a;
    --photo-van: linear-gradient(160deg, #9fb9c9 0%, #5f86a8 45%, #6d6f62 100%);
    --photo-olives: radial-gradient(circle at 40% 40%, #d3b15a 0%, #9a7a2c 45%, #5a2030 100%);
    --photo-gyro: linear-gradient(150deg, #7b7d74 0%, #caa97a 45%, #b07858 100%);
    --photo-halloumi: linear-gradient(180deg, #2a2724 0%, #e6dcc8 35%, #c4ae8d 60%, #2f2a26 100%);
    --photo-skewers: radial-gradient(circle at 45% 40%, #b99b7f 0%, #7a5b43 45%, #221a16 100%);
    --photo-dips: linear-gradient(160deg, #5b5a54 0%, #8c8a82 40%, #d9c28f 70%, #6f6c63 100%);
  }
  * { box-sizing: border-box; margin: 0; padding: 0; }
  html, body { width: 1200px; height: 1200px; overflow: hidden; background: var(--backdrop); }
  .canvas { position: relative; width: 1200px; height: 1200px; }
  .ad {
    position: absolute; left: 342px; top: 37px; width: 516px; height: 1126px;
    background: var(--paper); border: 4px solid var(--brand-blue);
  }
  .ad > * { position: absolute; }
  .brand-box {
    left: 171px; top: -4px; width: 167px; height: 177px; background: var(--brand-blue);
    display: flex; flex-direction: column; align-items: center; justify-content: center; gap: 12px;
  }
  .brand-dot { width: 26px; height: 26px; border-radius: 50%; background: var(--paper); }
  .brand-name {
    font-family: "Questrial", sans-serif; font-weight: 400; color: var(--paper); font-size: 21px;
    line-height: 1.15; text-align: center; letter-spacing: 1px; text-transform: uppercase;
  }
  .side-note {
    top: 34px; width: 136px; font-family: "Questrial", sans-serif; font-weight: 400;
    color: var(--brand-blue); font-size: 12px; line-height: 1.35;
  }
  .side-note .note-title {
    display: block; font-size: 11px; letter-spacing: 1.2px; text-transform: uppercase;
    border-bottom: 1px solid var(--brand-blue); padding-bottom: 4px; margin-bottom: 7px;
  }
  .featured { left: 22px; }
  .featured li { list-style: none; margin-bottom: 4px; }
  .social { left: 350px; }
  .social li { list-style: none; display: flex; align-items: center; gap: 6px; margin-bottom: 6px; }
  .social-dot { flex: none; width: 10px; height: 10px; border-radius: 50%; background: var(--brand-blue); }
  .web { font-size: 10.5px; }
  .headline {
    left: 29px; top: 176px; width: 450px; height: 68px; background: var(--brand-blue);
    color: var(--paper); font-family: "Questrial", sans-serif; font-weight: 400; font-size: 26px; line-height: 1.15;
    text-align: center; display: flex; align-items: center; justify-content: center;
  }
  .photo { display: block; }
  .photo-van { left: 29px; top: 249px; width: 237px; height: 175px; background: var(--photo-van); }
  .photo-olives { left: 272px; top: 249px; width: 207px; height: 202px; background: var(--photo-olives); }
  .photo-gyro { left: 89px; top: 429px; width: 177px; height: 190px; background: var(--photo-gyro); }
  .photo-halloumi { left: 272px; top: 457px; width: 207px; height: 201px; background: var(--photo-halloumi); }
  .photo-skewers { left: 29px; top: 625px; width: 237px; height: 241px; background: var(--photo-skewers); }
  .photo-dips { left: 272px; top: 664px; width: 207px; height: 153px; background: var(--photo-dips); }
  .body-copy {
    font-family: "Arimo", sans-serif; color: var(--body-ink); font-size: 9.6px; line-height: 1.32;
  }
  .body-copy p + p { margin-top: 7px; }
  .story-right { left: 281px; top: 826px; width: 200px; }
  .food-heading {
    left: 36px; top: 890px; font-family: "Questrial", sans-serif; font-weight: 400; color: var(--brand-blue);
    font-size: 33px; line-height: 1;
  }
  .story-left { left: 36px; top: 937px; width: 232px; }
  .offer-band {
    left: 29px; top: 1029px; width: 450px; height: 78px; background: var(--offer-red);
    color: var(--paper); font-family: "Questrial", sans-serif; text-align: center;
    display: flex; flex-direction: column; align-items: center; justify-content: center;
  }
  .offer-amount { font-size: 46px; line-height: 1; }
  .offer-expiry { font-size: 14px; letter-spacing: 0.5px; margin-top: 4px; }
  .offer-code { border: 1px solid var(--paper); padding: 0 5px; }
</style>
</head>
<body>
<div class="canvas">
  <article class="ad">
    <aside class="side-note featured">
      <span class="note-title">As featured in</span>
      <ul>
        <li>The Harbour Courier</li>
        <li>Streetside Eats</li>
        <li>Market Weekly</li>
      </ul>
    </aside>

    <div class="brand-box">
      <span class="brand-dot"></span>
      <span class="brand-name">The<br>Sizzling<br>Pelican</span>
    </div>

    <aside class="side-note social">
      <span class="note-title">Follow us</span>
      <ul>
        <li><span class="social-dot"></span>@sizzlingpelican</li>
        <li><span class="social-dot"></span>#sizzlingpelican</li>
        <li class="web"><span class="social-dot"></span>thesizzlingpelican.co.uk</li>
      </ul>
    </aside>

    <h1 class="headline">Authentic Greek food<br>on the streets of London</h1>

    <div class="photo photo-van" role="img" aria-label="Blue and white street food van parked outside"></div>
    <div class="photo photo-olives" role="img" aria-label="Bowl of green and Kalamata olives"></div>
    <div class="photo photo-gyro" role="img" aria-label="Grilled meat wrapped in pitta with red onion"></div>
    <div class="photo photo-halloumi" role="img" aria-label="Halloumi slices on a grill"></div>
    <div class="photo photo-skewers" role="img" aria-label="Meat skewers cooking on a barbecue"></div>
    <div class="photo photo-dips" role="img" aria-label="Olives and dip pots with pitta chips on a wooden table"></div>

    <div class="body-copy story-right">
      <p>It's with those fond memories that The Sizzling Pelican was born. We try and share those moments with everyone who tries our food. The meats we use are local, free range and halal(chicken). The produce like our vine tomatoes, herbs and potatoes are also local and where possible organic. We import only the highest quality Greek products like Extra virgin olive oil, barrel aged feta and Kalamata olives.</p>
      <p>Everything prepared and cooked fresh, on the day, for each event/market ensuring quality and authentic flavors.</p>
    </div>

    <h2 class="food-heading">The Food</h2>
    <div class="body-copy story-left">
      <p>Growing up in my house was like a festival of food. It was integral in every part of life from holidays to daily meals and everything in between. Everything was fresh, local and prepared with love and detail. The joy on people's faces when they tasted the various delicacies, was priceless.</p>
    </div>

    <div class="offer-band">
      <span class="offer-amount">10% OFF</span>
      <span class="offer-expiry">QUOTE <span class="offer-code">PELICAN10</span> · VALID UNTIL MARCH 2017</span>
    </div>
  </article>
</div>
</body>
</html>
```